Briefpapier und Visitenkarten
Zielgruppe
In erster Linie mir selbst.
Aufgabenstellung
Gestaltung von Visitenkarten und Briefpapier.
Visitenkarten: Gestaltung beidseitig und in Pantone Farben
Briefpapier: Gestaltung einseitig und in Pantone Farben
Briefpapier und Visitenkarten sollen ein Design haben.

```html
<!DOCTYPE html>
<html lang="de">
<head>
<meta charset="utf-8">
<title>Korland Werbeagentur – Briefpapier und Visitenkarten</title>
<link href="https://fonts.googleapis.com/css2?family=Arimo:wght@400;700&display=swap" rel="stylesheet">
<style>
  :root {
    --paper: #ffffff;
    --stage: #ffffff;
    --ink: #bfbfbf;
    --mark: #c6c6c6;
    --edge: #d6d6d6;
    --shadow: rgba(0,0,0,0.35);
  }
  * { margin: 0; padding: 0; box-sizing: border-box; }
  html, body { width: 1200px; height: 900px; overflow: hidden; background: var(--stage); }
  body { position: relative; font-family: "Arimo", Arial, sans-serif; color: var(--ink); }

  .sheet { position: absolute; background: var(--paper); border: 1px solid var(--edge); box-shadow: 3px 4px 6px var(--shadow); }
  .center { position: absolute; left: 0; right: 0; text-align: center; white-space: nowrap; }
  .brand-dot { position: absolute; left: 50%; border-radius: 50%; background: var(--mark); transform: translateX(-50%); }

  /* Briefbogen */
  .letterhead { left: 20px; top: 12px; width: 619px; height: 873px; }
  .letterhead .brand-dot { top: 27px; width: 35px; height: 35px; }
  .letterhead .brand-name { top: 66px; font-size: 15px; font-weight: 700; letter-spacing: 0.5px; }
  .letterhead .brand-claim { top: 85px; font-size: 5px; letter-spacing: 2.5px; text-transform: uppercase; }
  .sender-line { position: absolute; left: 70px; top: 131px; font-size: 5.5px; text-transform: uppercase; letter-spacing: 0.2px; white-space: nowrap; }
  .fold-mark { position: absolute; left: 0; width: 7px; height: 1px; background: var(--edge); }
  .fold-mark.upper { top: 304px; }
  .fold-mark.lower { top: 437px; }
  .letter-footer { top: 805px; font-size: 6.5px; line-height: 9px; }
  .letter-footer b { font-weight: 700; text-transform: uppercase; }

  /* Visitenkarten */
  .card { width: 479px; height: 309px; }
  .card-front { left: 689px; top: 218px; }
  .card-back { left: 687px; top: 562px; }
  .card .brand-dot { top: 21px; width: 66px; height: 66px; }
  .card-front .brand-name { top: 94px; font-size: 25px; font-weight: 700; letter-spacing: 0.8px; }
  .card-front .brand-claim { top: 124px; font-size: 8px; letter-spacing: 4.5px; text-transform: uppercase; }
  .person-name { top: 90px; font-size: 24px; font-weight: 700; letter-spacing: 0.6px; }
  .person-role { top: 119px; font-size: 12px; letter-spacing: 0.6px; }
  .card-contact { top: 252px; font-size: 14px; line-height: 19px; }
  .card-contact b { font-weight: 700; }
  .gap { display: inline-block; width: 12px; }
</style>
</head>
<body>

  <section class="sheet letterhead" aria-label="Briefbogen">
    <div class="brand-dot"></div>
    <div class="center brand-name">KORLAND WERBEAGENTUR</div>
    <div class="center brand-claim">Wir planen - Sie wachsen</div>
    <div class="sender-line">Korland Werbeagentur Ahornweg 23 D-41199 Velden</div>
    <div class="fold-mark upper"></div>
    <div class="fold-mark lower"></div>
    <div class="center letter-footer">
      <b>Korland Werbeagentur</b> Wir planen - Sie wachsen<br>
      <b>Geschäftsführer</b> Tobias Korland <span class="gap"></span><b>Ahornweg 23 <span class="gap"></span>D-41199 Velden</b><br>
      <b>Telefon</b> 09876.543 210 <span class="gap"></span><b>Fax</b> 09876.543 210 <span class="gap"></span><b>Email</b> korland@korlandwa.de <span class="gap"></span><b>Web</b> www.korlandwa.de<br>
      <b>Kreisbank Velden</b> <span class="gap"></span>BLZ 100 100 00 <span class="gap"></span>KTO. 12 345 678 <span class="gap"></span><b>USt.-IdNr.</b> 123456789
    </div>
  </section>

  <section class="sheet card card-front" aria-label="Visitenkarte Vorderseite">
    <div class="brand-dot"></div>
    <div class="center brand-name">KORLAND WERBEAGENTUR</div>
    <div class="center brand-claim">Wir planen - Sie wachsen</div>
    <div class="center card-contact">
      <b>AHORNWEG 23 <span class="gap"></span>D-41199 VELDEN</b><br>
      <b>WEB</b> www.korlandwa.de
    </div>
  </section>

  <section class="sheet card card-back" aria-label="Visitenkarte Rückseite">
    <div class="brand-dot"></div>
    <div class="center person-name">TOBIAS KORLAND</div>
    <div class="center person-role">GESCHÄFTSFÜHRER</div>
    <div class="center card-contact">
      <b>TELEFON</b> 09876.543 210 <span class="gap"></span><b>FAX</b> 09876.543 210<br>
      <b>EMAIL</b> korland@korlandwa.de <span class="gap"></span><b>WEB</b> www.korlandwa.de
    </div>
  </section>

</body>
</html>
```